A professional I.T consulting company requires a web design

Our company needs a fresh web design to help us drive our business forward. We are an Information Technology company who specialises in solutions based I.T delivery and consultations and who prides ourselves on our professional approach to business.

We would like a web site design from a designer who may be able to help us upload the site to WordPress and who may be interested in completing the "coding" section of the site (minimal coding). Although this is not essential to this project and won't factor into the decision making process.

A very thorough brief has been put together for this design project so very limited work is required in regards to content (the brief sets out all the content text - copy write material).

Please see the attached project documents for a copy of the brief

Target Market(s)

Please refer to the attached brief

Industry/Entity Type

Business

Requirements
Must have
• Please refer to the attached brief
Nice to have
Should not have

```html
<!DOCTYPE html>
<html lang="en">
<head>
<meta charset="utf-8">
<title>KORVEX – Support Services</title>
<link href="https://fonts.googleapis.com/css2?family=Arimo:wght@400;700&family=Open+Sans:wght@400;600;700&display=swap" rel="stylesheet">
<style>
:root{
  --blue:#1e9bd7;
  --blue-dark:#1a5a8a;
  --nav-top:#3299d3;
  --nav-bottom:#1b6ea8;
  --text:#8a8a8a;
  --bg:#f2f2f2;
  --box-bg:#ececec;
  --box-border:#d6d6d6;
  --footer:#3e3e3e;
  --footer-bar:#1b6ea8;
  --footer-text:#d4d4d4;
}
*{margin:0;padding:0;box-sizing:border-box}
html,body{width:1200px;height:2353px;overflow:hidden}
body{background:var(--bg);font-family:"Arimo",Arial,sans-serif;color:var(--text);position:relative}
.abs{position:absolute}

/* header */
.brand{left:56px;top:38px}
.brand-name{font-family:"Open Sans",sans-serif;font-weight:700;font-size:46px;color:var(--blue);line-height:1}
.social{display:flex;gap:8px}
.social span{width:30px;height:30px;border-radius:50%;display:block}
.header-social{left:980px;top:31px}
.call{left:942px;top:78px;display:flex;gap:10px;align-items:center}
.call-icon{width:36px;height:40px;border-radius:6px;background:var(--blue);display:flex;align-items:center;justify-content:center}
.call small{display:block;font-size:13px;letter-spacing:1px;color:#9a9a9a}
.call strong{display:block;font-family:"Open Sans",sans-serif;font-weight:400;font-size:23px;color:var(--blue);line-height:1}

/* nav */
.nav{left:0;top:135px;width:1200px;height:45px;background:linear-gradient(var(--nav-top),var(--nav-bottom))}
.nav a{position:absolute;top:0;height:45px;line-height:45px;color:#fff;font-size:14px;letter-spacing:1px;text-decoration:none}
.nav a.active{background:#16588a;padding:0 12px}
.search{left:919px;top:8px;width:160px;height:31px;background:#fff;border:0;padding:0 12px;font-size:14px;color:#bbb;line-height:31px}
.search-btn{left:1079px;top:8px;width:57px;height:31px;background:#13548a;display:flex;align-items:center;justify-content:center}

/* content */
.title{font-family:"Open Sans",sans-serif;font-size:27px;font-weight:400;color:var(--blue);display:flex;align-items:center;gap:10px;line-height:1.2}
.title b{font-weight:400;color:var(--blue-dark)}
.rule{height:1px;background:#d8d8d8}
.copy{font-size:17px;line-height:26px}
.copy p+p{margin-top:26px}
.box{background:var(--box-bg);border:1px solid var(--box-border);padding:10px 14px 10px 28px;font-size:14.5px;line-height:26px}
.box ul{list-style:none}
.box li{position:relative}
.box li::before{content:"→";position:absolute;left:-21px;color:var(--blue);font-weight:700}
.note{color:var(--blue);margin-top:4px}

.simple{left:653px;top:290px;width:472px;height:283px;border:1px solid var(--box-border);padding:10px}
.simple-inner{border:1px solid #cfcfcf;height:100%;padding:22px 26px;background:#eeeeee}
.simple h3{font-family:"Open Sans",sans-serif;font-weight:400;font-size:26px;color:var(--blue)}
.simple h3 b{font-weight:400;color:var(--blue-dark)}
.simple p{font-size:14.5px;line-height:26px;margin-top:14px}

/* footer */
.footer{left:0;top:1937px;width:1200px;height:382px;background:var(--footer)}
.footer h4{position:absolute;top:48px;color:#fff;font-size:17px;letter-spacing:1.5px;font-weight:400}
.footer .line{position:absolute;height:1px;background:#5a5a5a}
.quote{position:absolute;left:99px;display:flex;gap:22px}
.photo{width:98px;height:98px;border:4px solid #2a2a2a;background:linear-gradient(#c9c3bc,#8c7d70)}
.quote p{width:280px;font-size:12.5px;line-height:19px;color:var(--footer-text);letter-spacing:.5px}
.quote cite{display:block;font-style:normal;color:var(--blue);letter-spacing:1px}
.links{position:absolute;left:585px;top:88px;list-style:none}
.links li{font-size:16px;color:#fff;letter-spacing:1px;line-height:34px}
.links li::before{content:"›";margin-right:12px}
.loc{position:absolute;left:886px;font-size:14.5px;color:var(--footer-text);letter-spacing:1px;line-height:20px;display:flex;gap:12px}
.footer-social{position:absolute;left:893px;top:239px}
.footer-social span{background:#777;border:2px solid #999}
.bar{left:0;top:2319px;width:1200px;height:34px;background:var(--footer-bar);color:#fff;font-size:12px;letter-spacing:1px;line-height:34px}
</style>
</head>
<body>

<header>
  <div class="abs brand"><div class="brand-name">KORVEX</div></div>
  <div class="abs social header-social">
    <span style="background:#1a6fa8"></span><span style="background:#3ba0de"></span><span style="background:#2d5a9c"></span><span style="background:#e8962b"></span>
  </div>
  <div class="abs call">
    <div class="call-icon"><svg width="18" height="22" viewBox="0 0 18 22"><path d="M4 1h4l1 6-3 2c1 3 3 6 6 7l2-3 5 2v4c0 2-2 3-4 3C7 21 1 13 1 5 1 3 2 1 4 1z" fill="#fff"/></svg></div>
    <div><small>CALL US TOLL FREE</small><strong>1300 555 010</strong></div>
  </div>
  <nav class="abs nav">
    <a style="left:64px">HOME</a>
    <a style="left:146px">ABOUT US</a>
    <a style="left:257px">WHY KORVEX?</a>
    <a class="active" style="left:381px">SERVICES</a>
    <a style="left:504px">SOLUTIONS</a>
    <a style="left:626px">TECHNOLOGIES</a>
    <a style="left:784px">CONTACT</a>
    <div class="abs search">Search</div>
    <div class="abs search-btn"><svg width="22" height="22" viewBox="0 0 22 22"><circle cx="13" cy="9" r="6" fill="none" stroke="#fff" stroke-width="3"/><path d="M9 13 2 20" stroke="#fff" stroke-width="4"/></svg></div>
  </nav>
</header>

<main>
  <h2 class="abs title" style="left:86px;top:226px">SUPPORT <b>SERVICES</b>
    <svg width="30" height="30" viewBox="0 0 30 30"><path d="M4 26 18 12M6 4l20 20" stroke="#1a5a8a" stroke-width="5"/></svg></h2>
  <div class="abs rule" style="left:86px;top:267px;width:980px"></div>

  <div class="abs copy" style="left:86px;top:292px;width:518px">
    <p>Just like a voucher, KORVEX's block service hours entitle you to services upon redemption.</p>
    <p>This simple, easy to understand and flexible system allows our clients to purchase hours in block amounts and then use these hours when and if required. Hours can be redeemed against any of our customized services and are most commonly used for utilizing specialist resources to engineer solutions, perform routine and emergency maintenance programs or for simply providing onsite and remote support. Redemption of these purchased hours against services is based on a flat hourly rate and offers the following benefits:</p>
  </div>

  <div class="abs box" style="left:86px;top:627px;width:518px;height:335px">
    <ul>
      <li>Pre-paid hours never expire.</li>
      <li>Flexible and allows for greater control over time allocation</li>
      <li>Utilised only when and if required</li>
      <li>You only pay for what you need</li>
      <li>Hours are calculated on a flat hourly rate only (no hidden or additional charges)</li>
      <li>One hour equals One hour (regardless of if its onsite or remote assistance)</li>
      <li>Hours are calculated on a flat hourly rate only (no hidden or additional charges)</li>
      <li>If works are required outside of standard business hours, (8:30 am until 5:30 pm Monday to Friday) these services attract a 50% loading only.</li>
    </ul>
  </div>

  <h2 class="abs title" style="left:86px;top:987px">ONLINE <b>SERVICES</b>
    <svg width="26" height="22" viewBox="0 0 26 22"><circle cx="13" cy="11" r="3" fill="#1a5a8a"/><path d="M7 5a8 8 0 0 0 0 12M19 5a8 8 0 0 1 0 12" stroke="#1a5a8a" stroke-width="2.5" fill="none"/></svg></h2>
  <div class="abs copy" style="left:86px;top:1036px;width:518px">
    <p>Included in our Support Services package is access to our senior specialist technicians with specific I.T expertise who can attend your place of business to assist with any onsite I.T issue. In utilising our Onsite Support Service, you can rest assured that:</p>
  </div>
  <div class="abs box" style="left:86px;top:1156px;width:518px;height:292px">
    <ul>
      <li>The clock doesn't start ticking until our engineer arrives on site (so travel time is not charged)</li>
      <li>One hour equals One hour. (regardless of the technician or the work performed)</li>
      <li>All our technicians are fully qualified and highly experienced</li>
      <li>Our technicians understand and embrace specific on-site requirements</li>
      <li>for individual clients (i.e. site specific equipment and specifications, inductions and sign in requirements)</li>
    </ul>
    <p class="note">Please note: all our on-site services incur a minimum charge time of two hours onsite</p>
  </div>

  <h2 class="abs title" style="left:86px;top:1492px">CONSULTANCY <b>SERVICES</b>
    <svg width="22" height="18" viewBox="0 0 22 18"><rect x="1" y="4" width="20" height="13" rx="2" fill="#1a5a8a"/><rect x="7" y="1" width="8" height="4" fill="none" stroke="#1a5a8a" stroke-width="2"/></svg></h2>
  <div class="abs copy" style="left:86px;top:1541px;width:518px">
    <p>Do you need the expertise of a skilled I.T Engineer to assist with your I.T infrastructure development or other I.T project works? Then our Consultancy Service could be the right fit for your business.</p>
    <p>Access to our Consultancy Service is another inclusion within purchased Support Services hours and can be utilised to assist your business with specific project works or even with high level I.T Strategic planning.</p>
    <p>For more information on our Consultancy Services, please visit our Consultancy Services Pages (Hyper link this).</p>
  </div>

  <aside class="abs simple">
    <div class="simple-inner">
      <h3>Support. <b>Simple</b></h3>
      <p>We're here when you need us.</p>
      <p>Expert support, with your business in mind. We'll work with you to know your business and support your orgnisations technology goals.</p>
    </div>
  </aside>

  <h2 class="abs title" style="left:653px;top:598px;display:block">UNLIMITED REMOTE HELP<br><b>DESK SUPPORT</b>
    <svg width="22" height="20" viewBox="0 0 22 20" style="vertical-align:middle"><path d="M4 10a7 7 0 0 1 13-4M18 10a7 7 0 0 1-13 4" stroke="#1a5a8a" stroke-width="2.5" fill="none"/></svg></h2>
  <div class="abs copy" style="left:657px;top:679px;width:470px">
    <p>Hours purchased within our Support Services package can be utilised to access our popular service desk (help desk service) that entitles our clients access to all level 1 and level 2 I.T assistance requests. Use of this service is based on a flat hourly rate and includes the following benefits and/or conditions:</p>
  </div>
  <div class="abs box" style="left:651px;top:857px;width:474px;height:558px">
    <ul>
      <li>Allows access to instantaneous phone support when you need it</li>
      <li>All our Remote Help Desk Operators are highly focused on customer services and client satisfaction</li>
      <li>All our Remote Help Desk Operators are friendly, polite and very easy to talk to</li>
      <li>Minor I.T issues are resolved with maximum efficiency</li>
      <li>A maximum of forty five minutes is allocated to resolving issues remotely before escalating to onsite support (to ensure maximum solution efficiency).</li>
      <li>Issues are logged and recorded and analysis is provided in monthly reports</li>
      <li>All our remote support services are charged in fifteen minute increments against our flat hourly rate</li>
      <li>Purchased hours do not expire</li>
      <li>Remote Help Desk Support hours can be assigned on a month by month rolling contract with unused hours rolling over into the next month (month by month contracts can be exited at any time – no 'lock in' contracts)</li>
      <li>Any hours above the minimum allotment can be charged at the end of each month.</li>
    </ul>
  </div>
</main>

<footer class="abs footer">
  <h4 style="left:99px">TESTIMONIALS</h4>
  <div class="line" style="left:99px;top:73px;width:400px"></div>
  <div class="quote" style="top:88px">
    <div class="photo" role="img" aria-label="Portrait photo of a client"></div>
    <p>The staff at KORVEX are the most enthusiastic and personable people I have met and have an extensive IT knowledge and thirst for greater knowledge <cite>- DANIEL WHITMORE.</cite></p>
  </div>
  <div class="line" style="left:99px;top:211px;width:400px"></div>
  <div class="quote" style="top:222px">
    <div class="photo" role="img" aria-label="Portrait photo of a client"></div>
    <p>The staff at KORVEX are the most enthusiastic and personable people I have met and has an extensive IT knowledge and thirst for greater knowledge. <cite>- LUCAS BRENNAN.</cite></p>
  </div>
  <div class="line" style="left:99px;top:338px;width:400px"></div>
  <div style="position:absolute;left:106px;top:349px;color:#fff;font-size:13px;letter-spacing:1px">VIEW ALL</div>

  <h4 style="left:568px">QUICKLINKS</h4>
  <div class="line" style="left:568px;top:73px;width:230px"></div>
  <ul class="links">
    <li>Home</li><li>About us</li><li>Why KORVEX?</li><li>Services</li><li>Solutions</li><li>Technologies</li>
  </ul>

  <h4 style="left:886px">LOCATION</h4>
  <div class="line" style="left:886px;top:73px;width:230px"></div>
  <div class="loc" style="top:88px"><svg width="20" height="18" viewBox="0 0 20 18"><path d="M10 1 1 9h3v8h12V9h3z" fill="#ddd"/></svg><span>27 HARBOUR LANE.<br>WESTFIELD, CA<br>90210</span></div>
  <div class="loc" style="top:160px"><svg width="18" height="18" viewBox="0 0 18 18"><path d="M3 1h3l1 4-2 2c1 2 3 4 5 5l2-2 4 1v3c0 2-1 3-3 3C6 17 1 11 1 4c0-2 1-3 2-3z" fill="#ddd"/></svg><span>1300 555 010</span></div>
  <div class="loc" style="top:194px"><svg width="20" height="14" viewBox="0 0 20 14"><rect width="20" height="14" fill="#ddd"/><path d="M0 0l10 8 10-8" stroke="#3e3e3e" stroke-width="1.5" fill="none"/></svg><span>hello@korvexit.com</span></div>
  <div class="social footer-social"><span></span><span></span><span></span><span></span></div>
  <div class="line" style="left:886px;top:338px;width:230px"></div>
</footer>

<div class="abs bar">
  <span style="position:absolute;left:95px">Copyright 2014 · All rights reserved</span>
  <span style="position:absolute;left:882px">Sitemap &nbsp;&nbsp;| &nbsp;&nbsp;FAQ &nbsp;&nbsp;| &nbsp;&nbsp;Privacy Policy</span>
</div>

</body>
</html>
```